Marlow's Shutters VW Caddy Car Wrap Design

We need our VW Caddy Vans wrapped, 50%-75% of the vans covered.
We want our contact details (PH: 03)47196325, email: sales@marlowsshutters.com.au, web: www.marlowsshutters.com.au) included as well as our logo and images
Looking to incorporate our colours (green and grey) and some classy images.

Target Market(s)

All ages

Font styles to use
Serif
Sans Serif

Colors
00a990
edf8f6
474747
7f7f7f
32b8a4

Requirements
Must have
• Logo, Contact Details, colour scheme of Green and Grey, images
Should not have
• Hard to read, images to big that distracts from Logo/contact details

```html
<!DOCTYPE html>
<html lang="en">
<head>
<meta charset="utf-8">
<title>Marlow's Shutters – Van Wrap</title>
<link rel="stylesheet" href="https://fonts.googleapis.com/css2?family=Arimo:wght@400;700&display=swap">
<style>
  :root {
    --wrap-green: #1c6b34;
    --wrap-dark: #262626;
    --wrap-base: #f3f3f0;
    --wrap-edge: #d9d9d6;
    --pill-grey: #7c7c7c;
    --white: #ffffff;
    --page: #ffffff;
  }
  * { margin: 0; padding: 0; box-sizing: border-box; }
  html, body { width: 1200px; height: 1000px; overflow: hidden; background: var(--page); }
  .canvas { position: relative; width: 1200px; height: 1000px; }
  .wrap-shapes { position: absolute; inset: 0; }
  .brand-name {
    position: absolute; font-family: "Arimo", sans-serif; font-weight: 400;
    color: var(--wrap-green); font-size: 38px; line-height: 1; white-space: nowrap;
  }
  .tagline {
    position: absolute; font-family: "Arimo", sans-serif; font-weight: 400;
    color: var(--wrap-green); font-size: 20px; letter-spacing: 1px;
    line-height: 1; white-space: nowrap;
  }
  .service {
    position: absolute; width: 176px; height: 20px; background: var(--wrap-green);
    color: var(--white); font-family: "Arimo", sans-serif; font-weight: 700;
    font-size: 15px; line-height: 20px; text-align: center; letter-spacing: .3px;
  }
  .phone {
    position: absolute; font-family: "Arimo", sans-serif; font-weight: 700;
    color: var(--white); font-size: 31px; line-height: 1; white-space: nowrap;
  }
  .web {
    position: absolute; height: 36px; padding: 0 10px; background: var(--pill-grey);
    border-radius: 4px; color: var(--white); font-family: "Arimo", sans-serif;
    font-weight: 700; font-size: 18px; line-height: 36px; white-space: nowrap;
  }
  .email {
    position: absolute; font-family: "Arimo", sans-serif; color: var(--white);
    font-size: 13px; line-height: 1; white-space: nowrap;
  }
</style>
</head>
<body>
<main class="canvas">
  <svg class="wrap-shapes" width="1200" height="1000" viewBox="0 0 1200 1000" xmlns="http://www.w3.org/2000/svg">
    <defs>
      <linearGradient id="facade" x1="0" y1="0" x2="1" y2="1">
        <stop offset="0" stop-color="#d8d3ca"/>
        <stop offset="0.55" stop-color="#b9b8b3"/>
        <stop offset="1" stop-color="#8d9194"/>
      </linearGradient>
    </defs>

    <g class="panel panel-driver">
      <rect x="30" y="20" width="1120" height="420" rx="40" fill="var(--wrap-base)" stroke="var(--wrap-edge)" stroke-width="2"/>
      <polygon points="700,21 1060,21 935,250 625,250" fill="url(#facade)" role="img" aria-label="Photo of a building facade fitted with shutters"/>
      <polygon points="1060,21 1110,21 1148,60 1148,430 860,430 930,250" fill="var(--wrap-green)"/>
      <polygon points="625,250 930,250 860,438 495,438" fill="var(--wrap-dark)"/>
    </g>

    <g class="panel panel-passenger">
      <rect x="50" y="515" width="1120" height="420" rx="40" fill="var(--wrap-base)" stroke="var(--wrap-edge)" stroke-width="2"/>
      <polygon points="500,516 140,516 265,745 575,745" fill="url(#facade)" role="img" aria-label="Photo of a building facade fitted with shutters"/>
      <polygon points="140,516 90,516 52,555 52,925 340,925 270,745" fill="var(--wrap-green)"/>
      <polygon points="270,745 575,745 705,933 340,933" fill="var(--wrap-dark)"/>
    </g>
  </svg>

  <div class="brand-name" style="left:655px; top:96px;">Marlow's Shutters</div>
  <div class="tagline" style="left:657px; top:144px;">Shade made simple</div>
  <div class="service" style="left:352px; top:262px;">INTERNAL BLINDS</div>
  <div class="service" style="left:352px; top:293px;">EXTERNAL BLINDS</div>
  <div class="service" style="left:352px; top:338px;">CURTAINS</div>
  <div class="service" style="left:352px; top:367px;">MOTORISATION</div>
  <div class="phone" style="left:637px; top:272px;">(03) 4719 6325</div>
  <div class="web" style="left:560px; top:332px;">www.marlowsshutters.com.au</div>
  <div class="email" style="left:600px; top:376px;">sales@marlowsshutters.com.au</div>

  <div class="brand-name" style="left:210px; top:592px;">Marlow's Shutters</div>
  <div class="tagline" style="left:212px; top:640px;">Shade made simple</div>
  <div class="phone" style="left:318px; top:764px;">(03) 4719 6325</div>
  <div class="web" style="left:345px; top:826px;">www.marlowsshutters.com.au</div>
  <div class="email" style="left:385px; top:871px;">sales@marlowsshutters.com.au</div>
  <div class="service" style="left:669px; top:757px;">INTERNAL BLINDS</div>
  <div class="service" style="left:669px; top:788px;">EXTERNAL BLINDS</div>
  <div class="service" style="left:669px; top:833px;">CURTAINS</div>
  <div class="service" style="left:669px; top:861px;">MOTORISATION</div>
</main>
</body>
</html>
```